Lumo Cellar Traders needs a new business card design

Colour theme: Gold + Red preferred
Front side: Main logo with my details as below;
Back side: Theme of some wine glasses or bottles, maybe different color of log together
Lumo Cellar Traders

Leo Park
박 성민 (this is Korean character) on the English typying board: qkr tjdals
Managing Director

Suite 7/5 Harlow Rd
Bayfield WA 6923
Tel) +61(8) 6027 3518
Mob) +61(412) 305 276

leo.park@lumocellartraders.example
lumocellar@lumocellartraders.example
www.lumocellartraders.example

Target Market(s)

Asian Market

Industry/Entity Type

Business

Contact Information for Business Card

Lumo Cellar Traders

Leo Park
박 성민 (this is Korean character) English typying: qkr tjdals
Managing Director

Suite 7/5 Harlow Rd
Bayfield WA 6923
Tel) +61(8) 6027 3518
Mob) +61(412) 305 276

Font styles to use
Serif
Decorative

Colors
ec1f27
f78f21
f04a50
faa54b
cadf82
abd036

Requirements
Must have
• Company Logo & wine theme
Nice to have
• Very simple & modern
Should not have
• No Red Color on the name of Leo Park or 박 성민
• No traditional looking. young and modern look preferred

```html
<!DOCTYPE html>
<html lang="en">
<head>
<meta charset="utf-8">
<title>Lumo Cellar Traders — Business Card</title>
<link rel="stylesheet" href="https://fonts.googleapis.com/css2?family=Ropa+Sans&family=Tinos:wght@400;700&family=Nanum+Gothic&display=swap">
<style>
  :root {
    --stage: #2a2a2a;
    --red-top: #e03a27;
    --red-bottom: #b81f25;
    --red-accent: #c8202a;
    --icon-red: #e23a2c;
    --gold: #c3932e;
    --ink: #1a1a1a;
    --paper: #ffffff;
  }
  * { box-sizing: border-box; margin: 0; padding: 0; }
  html, body {
    width: 1189px; height: 1200px; overflow: hidden;
    background: var(--stage);
  }
  .card {
    position: absolute; left: 171px; width: 857px; height: 490px;
  }
  .card--front {
    top: 66px;
    background: linear-gradient(to bottom, var(--red-top), var(--red-bottom));
  }
  .card--back { top: 625px; background: var(--paper); }

  .brand-lockup {
    position: absolute; left: 0; right: 0; top: 200px;
    display: flex; flex-direction: column; align-items: center;
    color: var(--paper);
    font-family: "Ropa Sans", sans-serif;
  }
  .brand-lockup__row { display: flex; align-items: center; gap: 18px; }
  .brand-lockup__dot {
    width: 40px; height: 40px; border-radius: 50%; background: var(--paper);
  }
  .brand-lockup__name { font-size: 48px; letter-spacing: 1px; line-height: 1; }
  .brand-lockup__rule {
    width: 440px; height: 2px; background: var(--paper); margin: 12px 0 6px;
  }
  .brand-lockup__tagline { font-size: 20px; letter-spacing: 0.5px; }

  .back-brand {
    position: absolute; right: 55px; top: 62px; width: 360px;
    text-align: right; font-family: "Ropa Sans", sans-serif; color: var(--gold);
  }
  .back-brand__name { font-size: 46px; line-height: 0.98; letter-spacing: 1px; }
  .back-brand__rule { height: 2px; background: var(--red-accent); margin: 8px -6px 6px 0; }
  .back-brand__tagline { font-size: 23px; letter-spacing: 0.3px; }

  .contact {
    position: absolute; left: 45px; top: 176px;
    font-family: "Tinos", serif; color: var(--ink);
  }
  .contact__name { font-weight: 700; font-size: 30px; color: var(--gold); line-height: 1; }
  .contact__native { font-size: 23px; margin-top: 3px; line-height: 1.1; }
  .contact__native .ko { font-family: "Nanum Gothic", sans-serif; font-size: 21px; margin-right: 4px; }
  .contact__address { font-size: 23px; line-height: 27px; margin-top: 30px; }
  .contact__list { list-style: none; margin-top: 15px; }
  .contact__item {
    display: flex; align-items: center; gap: 8px;
    font-size: 23px; height: 28.7px;
  }
  .contact__icon { width: 26px; height: 26px; flex: none; }

  .website {
    position: absolute; right: 48px; bottom: 34px;
    font-family: "Tinos", serif; font-size: 22px; color: var(--ink);
  }
</style>
</head>
<body>
  <section class="card card--front">
    <div class="brand-lockup">
      <div class="brand-lockup__row">
        <span class="brand-lockup__dot"></span>
        <span class="brand-lockup__name">LUMO CELLAR TRADERS</span>
      </div>
      <div class="brand-lockup__rule"></div>
      <div class="brand-lockup__tagline">Connect &amp; Develop Your Business</div>
    </div>
  </section>

  <section class="card card--back">
    <div class="back-brand">
      <div class="back-brand__name">LUMO CELLAR<br>TRADERS</div>
      <div class="back-brand__rule"></div>
      <div class="back-brand__tagline">Connect &amp; Develop Your Business</div>
    </div>

    <div class="contact">
      <div class="contact__name">Leo Park</div>
      <div class="contact__native"><span class="ko">박 성민</span> qkr tjdals</div>
      <div class="contact__address">Suite 7/5 Harlow Rd<br>Bayfield WA 6923</div>
      <ul class="contact__list">
        <li class="contact__item">
          <svg class="contact__icon" viewBox="0 0 26 26" aria-hidden="true">
            <circle cx="13" cy="13" r="11.5" fill="none" stroke="var(--icon-red)" stroke-width="2"/>
            <path d="M7 11c0-2 3-3 6-3s6 1 6 3l-2 1-1-2h-6l-1 2z M9 13h8l1 5H8z" fill="var(--icon-red)"/>
          </svg>
          +61(8) 6027 3518
        </li>
        <li class="contact__item">
          <svg class="contact__icon" viewBox="0 0 26 26" aria-hidden="true">
            <circle cx="13" cy="13" r="11.5" fill="none" stroke="var(--icon-red)" stroke-width="2"/>
            <rect x="9.5" y="6.5" width="7" height="13" rx="1.5" fill="none" stroke="var(--icon-red)" stroke-width="1.8"/>
          </svg>
          +61(412) 305 276
        </li>
        <li class="contact__item">
          <svg class="contact__icon" viewBox="0 0 26 26" aria-hidden="true">
            <circle cx="13" cy="13" r="11.5" fill="none" stroke="var(--icon-red)" stroke-width="2"/>
            <rect x="7" y="9" width="12" height="8" fill="var(--icon-red)"/>
            <path d="M7 9l6 5 6-5" fill="none" stroke="#fff" stroke-width="1.2"/>
          </svg>
          leo.park@lumocellartraders.example
        </li>
        <li class="contact__item">
          <svg class="contact__icon" viewBox="0 0 26 26" aria-hidden="true">
            <circle cx="13" cy="13" r="11.5" fill="none" stroke="var(--icon-red)" stroke-width="2"/>
            <rect x="7" y="9" width="12" height="8" fill="var(--icon-red)"/>
            <path d="M7 9l6 5 6-5" fill="none" stroke="#fff" stroke-width="1.2"/>
          </svg>
          lumocellar@lumocellartraders.example
        </li>
      </ul>
    </div>

    <div class="website">www.lumocellartraders.example</div>
  </section>
</body>
</html>
```